pop up booking component and calendar re-design

we have a calander view where a parent cant reserve a day
you can click on please redesign the calander / voucher and pop up.

the dropdowns in pop up can be buttons
the dots on the calander indicate if there is space or not

when booking a day you can select a voucher

we used KIVO as inspiration, you are welcome to look at it as well.. screenshots attached

please ask questions if you have any

```html
<!DOCTYPE html>
<html lang="en">
<head>
<meta charset="utf-8">
<title>Booking calendar and book-day dialog</title>
<link href="https://fonts.googleapis.com/css2?family=Open+Sans:wght@300;400;600;700&display=swap" rel="stylesheet">
<style>
:root{
  --backdrop:#9b9d9c;
  --panel:#f6f5f3;
  --white:#ffffff;
  --ink:#2b2b2b;
  --muted:#6b6b6b;
  --teal:#23a3ba;
  --orange:#f15a24;
  --green:#2f8a17;
  --green-light:#55ad3d;
  --olive:#a8b41c;
  --head:#a1a8b4;
  --nav-grey:#8f9bab;
  --weekend:#f3f3f3;
  --booked:#e8f3f5;
  --line:#e3e3e3;
  --soft:#f3f2f3;
}
*{box-sizing:border-box;margin:0;padding:0}
html,body{width:1101px;height:1200px;overflow:hidden;background:var(--backdrop)}
body{font-family:"Open Sans",Arial,sans-serif;color:var(--ink)}
.stage{position:absolute;left:0;top:0;width:1848px;height:2014px;transform:scale(0.5958);transform-origin:0 0}

.screen{position:absolute;width:1676px;height:889px;background:var(--panel);overflow:hidden}
.screen--calendar{left:86px;top:68px}
.screen--dialog{left:83px;top:1025px}

.month-title{position:absolute;left:56px;top:40px;font-size:24px;font-weight:400}
.month-nav{position:absolute;left:885px;top:44px;height:37px;display:flex}
.month-nav__arrow{width:31px;background:var(--nav-grey);display:flex;align-items:center;justify-content:center}
.month-nav__today{width:77px;background:var(--teal);color:var(--white);font-size:14px;font-weight:600;display:flex;align-items:center;justify-content:center}

.calendar{position:absolute;left:56px;top:103px;width:968px}
.calendar__head{display:grid;grid-template-columns:repeat(7,1fr);height:43px;background:var(--head)}
.calendar__head span{color:var(--white);font-size:14px;font-weight:600;display:flex;align-items:center;justify-content:center;border-right:1px solid #b6bcc6}
.calendar__grid{display:grid;grid-template-columns:repeat(7,1fr);grid-auto-rows:127.5px;background:var(--white)}
.day{position:relative;border-right:1px solid var(--line);border-bottom:1px solid var(--line);background:var(--white)}
.day--weekend{background:var(--weekend)}
.day--booked{background:var(--booked)}
.day__num{position:absolute;right:16px;top:12px;font-size:25px;font-weight:300}
.day__dot{position:absolute;left:16px;top:22px;width:13px;height:13px;border-radius:50%;background:var(--teal)}
.day__dot--open{background:var(--olive)}
.day__info{position:absolute;left:13px;top:57px;font-size:13px;line-height:18px;color:var(--muted)}
.day__left{position:absolute;left:18px;top:64px;font-size:13px;color:var(--ink)}

.legend{position:absolute;left:52px;top:812px;display:flex;gap:26px;font-size:13px;font-weight:600}
.legend__item{display:flex;align-items:center;gap:9px}
.legend__item i{width:15px;height:15px;border-radius:50%;display:block}
.legend__item--away{color:var(--teal)}
.legend__item--away i{background:var(--teal)}
.legend__item--clear{color:#8c8c8c}
.legend__item--clear i{background:#a9a9a9}
.refresh{position:absolute;left:826px;top:810px}
.btn-cancel{position:absolute;left:885px;top:807px;width:138px;height:36px;background:var(--orange);color:var(--white);font-size:14px;font-weight:600;display:flex;align-items:center;justify-content:center}

.side-action{position:absolute;left:1068px;width:555px;height:66px;color:var(--white);font-size:20px;font-weight:700;letter-spacing:.5px;display:flex;align-items:center;justify-content:center;gap:16px}
.side-action--vouchers{top:103px;background:var(--teal)}
.side-action--purchase{top:189px;background:var(--orange)}
.side-action__count{width:34px;height:34px;border-radius:50%;background:var(--white);color:var(--orange);font-size:18px;display:flex;align-items:center;justify-content:center}

.voucher{position:absolute;left:1068px;width:555px;height:192px;background:var(--white);overflow:hidden}
.voucher--one{top:289px}
.voucher--two{top:516px}
.voucher__notch{position:absolute;left:160px;width:18px;height:18px;border-radius:50%;background:var(--panel)}
.voucher__notch--top{top:-9px}
.voucher__notch--bottom{bottom:-9px}
.voucher__divider{position:absolute;left:169px;top:18px;bottom:18px;border-left:2px dotted #bdbdbd}
.voucher__price{position:absolute;left:0;width:176px;top:58px;text-align:center;font-size:30px;font-weight:600}
.voucher__was{position:absolute;left:0;width:206px;top:104px;text-align:center;font-size:16px;color:#8a8a8a;text-decoration:line-through}
.voucher__tag{position:absolute;left:216px;top:25px;height:26px;padding:0 6px;border:2px solid var(--green);border-radius:3px;color:var(--green);font-size:13px;font-weight:700;display:flex;align-items:center}
.voucher__title{position:absolute;left:218px;top:66px;font-size:20px;font-weight:600}
.voucher__valid{position:absolute;left:218px;top:97px;font-size:16px;color:var(--muted)}
.voucher__buy{position:absolute;left:218px;top:138px;width:93px;height:28px;background:var(--orange);color:var(--white);font-size:12px;font-weight:700;display:flex;align-items:center;justify-content:center}
.voucher__rate{position:absolute;right:-48px;top:-104px;width:200px;height:200px;border-radius:50%;background:var(--green);color:var(--white)}
.voucher__rate span{position:absolute;left:24px;width:120px;text-align:center}
.voucher__rate .hrs{top:114px;font-size:16px}
.voucher__rate .amt{top:134px;font-size:23px;font-weight:700}

.dim{position:absolute;inset:0;background:rgba(38,38,38,.74)}

.dialog{position:absolute;left:277px;top:148px;width:1118px;height:507px;background:var(--white)}
.dialog__close{position:absolute;left:1078px;top:13px}
.tabs{position:absolute;left:37px;top:38px;display:flex;height:59px}
.tab{padding:0 29px;font-size:17px;font-weight:700;display:flex;align-items:center}
.tab--active{background:#f1efef;width:148px;justify-content:center;padding:0}
.booking{position:absolute;left:37px;top:97px;width:1050px;height:373px;border:2px solid #f1e9ea}
.booking__availability{position:absolute;left:27px;top:26px;font-size:16px}
.field-label{position:absolute;top:86px;font-size:16px;font-weight:600}
.select{position:absolute;top:118px;width:227px;height:50px;background:var(--soft);border:1px solid #cfcfcf;font-size:16px;padding-left:15px;display:flex;align-items:center}
.select svg{position:absolute;right:20px;top:22px}
.toggle{position:absolute;left:551px;top:116px;width:105px;height:55px;border-radius:28px;background:#c9c9c9}
.toggle i{position:absolute;left:11px;top:10px;width:35px;height:35px;border-radius:50%;background:var(--white)}
.slot{position:absolute;top:203px;width:120px;height:50px;background:#eeeeee;font-size:16px;font-weight:600;display:flex;align-items:center}
.slot__name{flex:1;text-align:center}
.slot__qty{width:52px;height:100%;background:var(--green);color:var(--white);font-weight:700;display:flex;align-items:center;justify-content:center}
.slot--full{background:var(--green);color:var(--white)}
.slot--full .slot__qty{background:var(--green-light)}
.slot--plain .slot__name{text-align:center}
.btn-close{position:absolute;left:31px;top:293px;width:96px;height:37px;background:var(--orange);color:var(--white);font-size:14px;font-weight:600;display:flex;align-items:center;justify-content:center}
.summary{position:absolute;left:727px;top:0;width:321px;height:369px;background:var(--soft)}
.summary__row{position:absolute;left:49px;right:49px;display:flex;justify-content:space-between;align-items:center;font-size:16px;font-weight:600}
.summary__row b{font-size:26px;font-weight:700}
.summary__rule{position:absolute;left:49px;right:49px;height:2px;background:#e2dfe0}
.btn-apply{width:70px;height:27px;background:var(--green);color:var(--white);font-size:14px;font-weight:700;display:flex;align-items:center;justify-content:center}
.btn-confirm{position:absolute;left:56px;top:280px;width:213px;height:54px;background:var(--teal);color:var(--white);font-size:22px;font-weight:600;display:flex;align-items:center;justify-content:center}
</style>
</head>
<body>
<div class="stage">

  <!-- Calendar view -->
  <section class="screen screen--calendar">
    <h1 class="month-title">October 2019</h1>
    <div class="month-nav">
      <span class="month-nav__arrow"><svg width="8" height="12"><path d="M6 1L2 6l4 5" fill="none" stroke="#fff" stroke-width="1.6"/></svg></span>
      <span class="month-nav__today">TODAY</span>
      <span class="month-nav__arrow"><svg width="8" height="12"><path d="M2 1l4 5-4 5" fill="none" stroke="#fff" stroke-width="1.6"/></svg></span>
    </div>

    <div class="calendar">
      <div class="calendar__head"><span>SUN</span><span>MON</span><span>TUE</span><span>WED</span><span>THU</span><span>FRI</span><span>SAT</span></div>
      <div class="calendar__grid">
        <div class="day day--weekend"></div>
        <div class="day"></div>
        <div class="day day--booked"><i class="day__dot"></i><span class="day__num">01</span><p class="day__info">LMK-3-Penguins<br>07:30 - 18:30<br>98:23</p></div>
        <div class="day day--booked"><i class="day__dot"></i><span class="day__num">02</span><p class="day__info">LMK-3-Penguins<br>07:30 - 18:30<br>98:23</p></div>
        <div class="day"><span class="day__num">03</span></div>
        <div class="day"><span class="day__num">04</span></div>
        <div class="day day--weekend"><span class="day__num">05</span></div>

        <div class="day day--weekend"><span class="day__num">06</span></div>
        <div class="day day--booked"><i class="day__dot"></i><span class="day__num">07</span><p class="day__info">LMK-3-Penguins<br>07:30 - 18:30<br>98:23</p></div>
        <div class="day day--booked"><i class="day__dot"></i><span class="day__num">08</span><p class="day__info">LMK-3-Penguins<br>07:30 - 18:30<br>98:23</p></div>
        <div class="day day--booked"><i class="day__dot"></i><span class="day__num">09</span><p class="day__info">LMK-3-Penguins<br>07:30 - 18:30<br>98:23</p></div>
        <div class="day"><span class="day__num">10</span></div>
        <div class="day"><span class="day__num">11</span></div>
        <div class="day day--weekend"><span class="day__num">12</span></div>

        <div class="day day--weekend"><span class="day__num">13</span></div>
        <div class="day day--booked"><i class="day__dot"></i><span class="day__num">14</span><p class="day__info">LMK-3-Penguins<br>07:30 - 18:30<br>98:23</p></div>
        <div class="day day--booked"><i class="day__dot"></i><span class="day__num">15</span><p class="day__info">LMK-3-Penguins<br>07:30 - 18:30<br>98:23</p></div>
        <div class="day day--booked"><i class="day__dot"></i><span class="day__num">16</span><p class="day__info">LMK-3-Penguins<br>07:30 - 18:30<br>98:23</p></div>
        <div class="day"><i class="day__dot day__dot--open"></i><span class="day__num">17</span><p class="day__left">0m/0a left</p></div>
        <div class="day"><i class="day__dot day__dot--open"></i><span class="day__num">18</span><p class="day__left">0m/0a left</p></div>
        <div class="day day--weekend"><span class="day__num">19</span></div>

        <div class="day day--weekend"><span class="day__num">20</span></div>
        <div class="day day--booked"><i class="day__dot"></i><span class="day__num">21</span><p class="day__info">LMK-3-Penguins<br>07:30 - 18:30<br>98:23</p></div>
        <div class="day day--booked"><i class="day__dot"></i><span class="day__num">22</span><p class="day__info">LMK-3-Penguins<br>07:30 - 18:30<br>98:23</p></div>
        <div class="day day--booked"><i class="day__dot"></i><span class="day__num">23</span><p class="day__info">LMK-3-Penguins<br>07:30 - 18:30<br>98:23</p></div>
        <div class="day"><i class="day__dot day__dot--open"></i><span class="day__num">24</span><p class="day__left">0m/0a left</p></div>
        <div class="day"><i class="day__dot day__dot--open"></i><span class="day__num">25</span><p class="day__left">0m/0a left</p></div>
        <div class="day day--weekend"><span class="day__num">26</span></div>

        <div class="day day--weekend"><span class="day__num">27</span></div>
        <div class="day day--booked"><i class="day__dot"></i><span class="day__num">28</span><p class="day__info">LMK-3-Penguins<br>07:30 - 18:30<br>98:23</p></div>
        <div class="day"><span class="day__num">29</span></div>
        <div class="day"><span class="day__num">30</span></div>
        <div class="day"></div>
        <div class="day"></div>
        <div class="day day--weekend"></div>
      </div>
    </div>

    <div class="legend">
      <span class="legend__item legend__item--away"><i></i>NOT COMING</span>
      <span class="legend__item legend__item--clear"><i></i>UNSELECT</span>
    </div>
    <svg class="refresh" width="34" height="34" viewBox="0 0 34 34"><path d="M5 15a12 12 0 0 1 22-6M29 19a12 12 0 0 1-22 6" fill="none" stroke="#8a8a8a" stroke-width="2.4"/><path d="M27 2v8h-8M7 32v-8h8" fill="none" stroke="#8a8a8a" stroke-width="2.4"/></svg>
    <span class="btn-cancel">CANCEL</span>

    <div class="side-action side-action--vouchers">VOUCHERS / PROMOTIONS</div>
    <div class="side-action side-action--purchase">PURCHASE <span class="side-action__count">2</span></div>

    <article class="voucher voucher--one">
      <i class="voucher__notch voucher__notch--top"></i><i class="voucher__notch voucher__notch--bottom"></i><i class="voucher__divider"></i>
      <p class="voucher__price">€ 89.00</p><p class="voucher__was">€94.00</p>
      <span class="voucher__tag">15% OFF</span>
      <h2 class="voucher__title">Booking Test Promo</h2>
      <p class="voucher__valid">Valid till 15th Dec 2019</p>
      <span class="voucher__buy">PURCHASE</span>
      <div class="voucher__rate"><span class="hrs">10 hours</span><span class="amt">@ € 8.9</span></div>
    </article>
    <article class="voucher voucher--two">
      <i class="voucher__notch voucher__notch--top"></i><i class="voucher__notch voucher__notch--bottom"></i><i class="voucher__divider"></i>
      <p class="voucher__price">€ 80.37</p><p class="voucher__was">€94.00</p>
      <span class="voucher__tag">15% OFF</span>
      <h2 class="voucher__title">Test Lab Promotion</h2>
      <p class="voucher__valid">Valid till 15th Dec 2019</p>
      <span class="voucher__buy">PURCHASE</span>
      <div class="voucher__rate"><span class="hrs">10 hours</span><span class="amt">@ € 8.93</span></div>
    </article>
  </section>

  <!-- Calendar view with book-day dialog open -->
  <section class="screen screen--dialog">
    <h1 class="month-title">October 2019</h1>
    <div class="month-nav">
      <span class="month-nav__arrow"><svg width="8" height="12"><path d="M6 1L2 6l4 5" fill="none" stroke="#fff" stroke-width="1.6"/></svg></span>
      <span class="month-nav__today">TODAY</span>
      <span class="month-nav__arrow"><svg width="8" height="12"><path d="M2 1l4 5-4 5" fill="none" stroke="#fff" stroke-width="1.6"/></svg></span>
    </div>
    <div class="calendar">
      <div class="calendar__head"><span>SUN</span><span>MON</span><span>TUE</span><span>WED</span><span>THU</span><span>FRI</span><span>SAT</span></div>
      <div class="calendar__grid">
        <div class="day day--weekend"></div><div class="day"></div>
        <div class="day day--booked"></div><div class="day day--booked"></div>
        <div class="day"></div><div class="day"></div><div class="day day--weekend"></div>

        <div class="day day--weekend"><span class="day__num">06</span></div>
        <div class="day day--booked"><i class="day__dot"></i><p class="day__info">LMK-3-Penguins<br>07:30 - 18:30<br>98:23</p></div>
        <div class="day day--booked"></div><div class="day day--booked"></div>
        <div class="day"></div><div class="day"></div><div class="day day--weekend"></div>

        <div class="day day--weekend"><span class="day__num">13</span></div>
        <div class="day day--booked"><i class="day__dot"></i><p class="day__info">LMK-3-Penguins<br>07:30 - 18:30<br>98:23</p></div>
        <div class="day day--booked"></div><div class="day day--booked"></div>
        <div class="day"></div><div class="day"></div><div class="day day--weekend"></div>

        <div class="day day--weekend"><span class="day__num">20</span></div>
        <div class="day day--booked"><i class="day__dot"></i><p class="day__info">LMK-3-Penguins<br>07:30 - 18:30<br>98:23</p></div>
        <div class="day day--booked"></div><div class="day day--booked"></div>
        <div class="day"></div><div class="day"></div><div class="day day--weekend"></div>

        <div class="day day--weekend"><span class="day__num">27</span></div>
        <div class="day day--booked"><i class="day__dot"></i><span class="day__num">28</span><p class="day__info">LMK-3-Penguins<br>07:30 - 18:30<br>98:23</p></div>
        <div class="day"><span class="day__num">29</span></div>
        <div class="day"><span class="day__num">30</span></div>
        <div class="day"></div><div class="day"></div><div class="day day--weekend"></div>
      </div>
    </div>
    <div class="legend">
      <span class="legend__item legend__item--away"><i></i>NOT COMING</span>
      <span class="legend__item legend__item--clear"><i></i>UNSELECT</span>
    </div>
    <svg class="refresh" width="34" height="34" viewBox="0 0 34 34"><path d="M5 15a12 12 0 0 1 22-6M29 19a12 12 0 0 1-22 6" fill="none" stroke="#8a8a8a" stroke-width="2.4"/><path d="M27 2v8h-8M7 32v-8h8" fill="none" stroke="#8a8a8a" stroke-width="2.4"/></svg>
    <span class="btn-cancel">CANCEL</span>
    <div class="side-action side-action--vouchers">VOUCHERS / PROMOTIONS</div>
    <div class="side-action side-action--purchase">PURCHASE <span class="side-action__count">2</span></div>
    <article class="voucher voucher--one">
      <i class="voucher__notch voucher__notch--top"></i><i class="voucher__notch voucher__notch--bottom"></i><i class="voucher__divider"></i>
      <h2 class="voucher__title">Booking Test Promo</h2>
      <p class="voucher__valid">Valid till 15th Dec 2019</p>
      <div class="voucher__rate"><span class="hrs">10 hours</span><span class="amt">@ € 8.9</span></div>
    </article>
    <article class="voucher voucher--two">
      <i class="voucher__notch voucher__notch--top"></i><i class="voucher__notch voucher__notch--bottom"></i><i class="voucher__divider"></i>
      <h2 class="voucher__title">Test Lab Promotion</h2>
      <p class="voucher__valid">Valid till 15th Dec 2019</p>
      <span class="voucher__buy">PURCHASE</span>
      <div class="voucher__rate"><span class="hrs">10 hours</span><span class="amt">@ € 8.93</span></div>
    </article>

    <div class="dim"></div>

    <div class="dialog" role="dialog" aria-label="Book day">
      <svg class="dialog__close" width="28" height="28" viewBox="0 0 28 28"><circle cx="14" cy="14" r="13" fill="#6f6f6f"/><path d="M9 9l10 10M19 9L9 19" stroke="#fff" stroke-width="3"/></svg>
      <div class="tabs">
        <span class="tab tab--active">BOOK DAY</span>
        <span class="tab">VOUCHERS</span>
      </div>
      <div class="booking">
        <p class="booking__availability">Availability : 1m/1a left &nbsp;|&nbsp; 24-10-2019</p>
        <span class="field-label" style="left:27px">LOCATION</span>
        <span class="field-label" style="left:280px">GROUPS</span>
        <span class="field-label" style="left:551px">BSO</span>
        <div class="select" style="left:29px">LMK<svg width="12" height="7"><path d="M0 0h12L6 7z" fill="#222"/></svg></div>
        <div class="select" style="left:282px">3 PENGUINS<svg width="12" height="7"><path d="M0 0h12L6 7z" fill="#222"/></svg></div>
        <div class="toggle"><i></i></div>

        <div class="slot slot--full" style="left:30px"><span class="slot__name">FULL</span><span class="slot__qty">1</span></div>
        <div class="slot" style="left:159px"><span class="slot__name">AM</span><span class="slot__qty">1</span></div>
        <div class="slot" style="left:290px"><span class="slot__name">PM</span><span class="slot__qty">1</span></div>
        <div class="slot slot--plain" style="left:421px"><span class="slot__name">FLEX</span></div>
        <div class="slot slot--plain" style="left:552px"><span class="slot__name">TRY</span></div>

        <span class="btn-close">CLOSE</span>

        <div class="summary">
          <div class="summary__row" style="top:44px"><span>PRICE</span><b>€ 89.00</b></div>
          <i class="summary__rule" style="top:95px"></i>
          <div class="summary__row" style="top:120px"><span>VOUCHER</span><span class="btn-apply">APPLY</span></div>
          <i class="summary__rule" style="top:174px"></i>
          <div class="summary__row" style="top:196px"><span>TOTAL</span><b>€ 98.23</b></div>
          <span class="btn-confirm">CONFIRM</span>
        </div>
      </div>
    </div>
  </section>

</div>
</body>
</html>
```